Book Cover for Self Help Book Teens

I need a standard a5 size book cover (front and back) for my new self help book for teens. The book is called
WHEN DAYS DRAG
ideas and tactics for teens in tough times
break ups, school problems, procrastination, fights, sexuality, alcohol, bitchiness, eating problems, can’t sleep, no motivation, not allowed to do stuff, being on the outer..and 34 other common situations that every day Australian teens face
Marisol Penhale
psychologist for teens
I would like a very sparse,very modern cover, no photos - maybe just cartoon-y graphic of smiley face upside down - ie frowny face. Few colours in order to make it look bold. lots of space on the cover.
I will provide back cover text soon
Updates
I just want to say that I really appreciate all of your efforts, the designs were excellent. As a thankyou, I'm happy to email you a link to the e-version of this book if you are interested. Just email me at marisolpenhale@brightwavemail.net and I will send it through as soon as it is completed.
Target Market(s)
teens....but parents will also be buying book
Industry/Entity Type
School
Look and feel

```html
<!DOCTYPE html>
<html lang="en">
<head>
<meta charset="utf-8">
<title>When Days Drag – Front Cover</title>
<link rel="stylesheet" href="https://fonts.googleapis.com/css2?family=Jost:wght@400;600;700&family=Nothing+You+Could+Do&display=swap">
<style>
  :root {
    --page-bg: #ffffff;
    --label-ink: #111111;
    --cover-maroon: #721c3b;
    --maze-orange: #f07d00;
    --maze-orange-deep: #c9640a;
    --cover-white: #ffffff;
  }

  html, body {
    margin: 0;
    padding: 0;
    width: 1200px;
    height: 909px;
    overflow: hidden;
    background: var(--page-bg);
  }

  .canvas {
    position: relative;
    width: 1200px;
    height: 909px;
  }

  .side-label {
    position: absolute;
    left: 60px;
    top: 91px;
    margin: 0;
    font-family: "Jost", sans-serif;
    font-weight: 400;
    font-size: 18px;
    line-height: 22px;
    letter-spacing: 1.5px;
    color: var(--label-ink);
  }

  .cover {
    position: absolute;
    left: 326px;
    top: 50px;
    width: 555px;
    height: 794px;
    background: var(--cover-maroon);
  }

  .cover-art {
    position: absolute;
    left: 0;
    top: 0;
    width: 555px;
    height: 794px;
  }

  .cover-title {
    font-family: "Jost", sans-serif;
    font-weight: 700;
    font-size: 21px;
    letter-spacing: 1.5px;
    fill: var(--cover-white);
  }

  .cover-subtitle {
    position: absolute;
    left: 0;
    top: 621px;
    width: 555px;
    margin: 0;
    text-align: center;
    white-space: nowrap;
    font-family: "Nothing You Could Do", cursive;
    font-size: 27px;
    line-height: 47px;
    color: var(--cover-white);
  }

  .cover-author {
    position: absolute;
    left: 0;
    top: 733px;
    width: 555px;
    margin: 0;
    text-align: center;
    font-family: "Jost", sans-serif;
    font-weight: 600;
    font-size: 15px;
    line-height: 22px;
    letter-spacing: 1px;
    color: var(--cover-white);
  }
</style>
</head>
<body>
<main class="canvas">
  <p class="side-label">FRONT</p>

  <section class="cover" aria-label="Front cover">
    <svg class="cover-art" viewBox="0 0 555 794" xmlns="http://www.w3.org/2000/svg">
      <defs>
        <radialGradient id="maze-tone" cx="50%" cy="50%" r="50%">
          <stop offset="0%" stop-color="#c9640a"/>
          <stop offset="100%" stop-color="#f07d00"/>
        </radialGradient>
        <path id="title-arc" d="M 92 348 A 185 185 0 0 1 462 348"/>
      </defs>
      <circle class="maze-area" cx="277" cy="348" r="223" fill="url(#maze-tone)"
              role="img" aria-label="Circular orange maze with a winding white path leading to a smiley at its centre"/>
      <text class="cover-title" text-anchor="middle">
        <textPath href="#title-arc" startOffset="50%">WHEN DAYS DRAG</textPath>
      </text>
    </svg>

    <p class="cover-subtitle">ideas and tactics<br>for teens in tough times</p>
    <p class="cover-author">MARISOL PENHALE</p>
  </section>
</main>
</body>
</html>
```